Podcast cover art (not a logo)

I’m launching an audio-only podcast for parents of neurodivergent children. The podcast is meant to feel like a calm, trusted professional voice — not a brand or a performance.

Style direction:
--Clean and minimal
--Calm and grounded
--Professional, not playful
--Nothing flashy, loud, or busy
--No cartoon imagery

Content on the cover:
--Podcast title: Under the Quiet Surface
--Subtitle or tagline: Supporting Neurodivergent Kids with Science, Not Shame (or Understanding Neurodivergent Kids)
--No episode numbers, no dates

Design preferences:
--Text-forward design
--Neutral or soft colors (muted blues, grays, off-whites)
--High contrast for readability at small sizes
--Simple, timeless font

What I do NOT want:
--A logo or branding system
--Illustrations of children or families
--Bright colors or playful graphics
--Trendy fonts or visual effects

Technical requirements:
--Square image
--3000 × 3000 pixels
--RGB color mode
--JPEG or PNG
--File size under 500 KB

Deliverables:
--Final cover art file
--Optional: one or two alternate background color versions

```html
<!DOCTYPE html>
<html lang="en">
<head>
<meta charset="utf-8">
<title>Under the Quiet Surface — Podcast Cover</title>
<link href="https://fonts.googleapis.com/css2?family=Source+Serif+4:opsz,wght@8..60,400&display=swap" rel="stylesheet">
<style>
  :root {
    --backdrop: #d3d8dc;
    --card: #f2f0ea;
    --ink: #3a4f5f;
    --artboard: 3000px;   /* true export size: 3000 × 3000 */
    --preview-scale: 0.4; /* 3000 × 0.4 = 1200 preview canvas */
  }
  html, body {
    margin: 0;
    padding: 0;
    width: 1200px;
    height: 1200px;
    overflow: hidden;
    background: var(--backdrop);
  }
  .cover {
    position: relative;
    width: var(--artboard);
    height: var(--artboard);
    background: var(--backdrop);
    transform: scale(var(--preview-scale));
    transform-origin: 0 0;
  }
  .cover-card {
    position: absolute;
    left: 240px;
    top: 272px;
    width: 2522px;
    height: 2458px;
    background: var(--card);
    border-radius: 30px;
  }
  .show-title {
    position: absolute;
    left: 512px;
    top: 560px;
    margin: 0;
    font-family: "Source Serif 4", Georgia, serif;
    font-weight: 400;
    font-size: 505px;
    line-height: 480px;
    letter-spacing: -2px;
    color: var(--ink);
    white-space: nowrap;
  }
  .show-title span { display: block; }
  .show-tagline {
    position: absolute;
    left: 520px;
    top: 2150px;
    margin: 0;
    font-family: "Source Serif 4", Georgia, serif;
    font-weight: 400;
    font-size: 125px;
    line-height: 165px;
    color: var(--ink);
    white-space: nowrap;
  }
  .show-tagline span { display: block; }
</style>
</head>
<body>
  <main class="cover">
    <section class="cover-card"></section>
    <h1 class="show-title">
      <span>Under</span>
      <span>the Quiet</span>
      <span>Surface</span>
    </h1>
    <p class="show-tagline">
      <span>Supporting Neurodivergent Kids</span>
      <span>with Science, Not Shame</span>
    </p>
  </main>
</body>
</html>
```